Business Card Design

I am a nail technician. I want my logo to be Mia Adores Polish. I would like the loves to be a hot pink or red heart. I would like the rest of the text in black. It must look classy and slick and the heart must pop out across the middle of the information side of the card.

I would like this side of my card to have the above information and the uploaded VRT logo to the bottom left hand corner.

I would like one side of the card to say 'Nails are jewels not tools' in same colour that is used for the heart in loves part of logo

Target Market(s)

Women who get nails done

Industry/Entity Type

Business

Contact Information for Business Card

Title in middle of card- Mia Adores (preferably a heart rather than the word) Nails. Under this Nail Technician, I would like this central.

To right hand bottom corner- Mia Penhallow, mob-07700283614, email-miaadorespolish@brightpost.example

Requirements
Must have
• The heart in Mia 'adores' polish

I want it to be all black and white apart from the pink/red heart in the loves and 'nails are jewels not tools' happy to go with whatever pops off the card the most and draws the eye

```html
<!DOCTYPE html>
<html lang="en">
<head>
<meta charset="utf-8">
<title>Mia Adores Polish – Business Card</title>
<link rel="stylesheet" href="https://fonts.googleapis.com/css2?family=Questrial&family=Arimo:wght@400&display=swap">
<style>
  :root {
    --backdrop: #2b2b2b;
    --card: #ffffff;
    --ink: #111111;
    --pink: #ee2a86;
    --rule: #9a9a9a;
  }
  * { box-sizing: border-box; margin: 0; padding: 0; }
  html, body {
    width: 1200px; height: 900px; overflow: hidden;
    background: var(--backdrop);
  }
  .canvas {
    position: relative; width: 1200px; height: 900px;
    display: flex; align-items: center; justify-content: center; gap: 50px;
  }
  .card {
    position: relative; width: 520px; height: 315px;
    background: var(--card);
    box-shadow: 0 10px 30px rgba(0,0,0,.45);
  }
  .wordmark {
    display: flex; align-items: center; justify-content: center; gap: 14px;
    font-family: "Questrial", sans-serif; color: var(--ink);
    font-size: 40px; letter-spacing: .5px; white-space: nowrap;
  }
  .wordmark__dot {
    width: 52px; height: 52px; border-radius: 50%; background: var(--pink);
    flex: none;
  }

  /* tagline side */
  .card--tagline .wordmark { margin-top: 104px; }
  .tagline {
    margin-top: 14px; text-align: center;
    font-family: "Questrial", sans-serif; color: var(--pink); font-size: 19px;
  }

  /* information side */
  .card--info { border-left: 14px solid var(--ink); }
  .card--info .wordmark { margin-top: 52px; font-size: 42px; }
  .card--info .wordmark__dot { width: 58px; height: 58px; }
  .job-title {
    margin-top: 10px; text-align: center;
    font-family: "Questrial", sans-serif; color: var(--ink); font-size: 22px;
  }
  .partner {
    position: absolute; left: 30px; bottom: 44px;
    display: flex; align-items: center; gap: 8px;
    font-family: "Questrial", sans-serif; color: var(--ink);
    font-size: 44px; letter-spacing: 1px;
  }
  .partner__square { width: 32px; height: 32px; background: var(--ink); }
  .divider {
    position: absolute; left: 206px; bottom: 30px;
    width: 1px; height: 80px; background: var(--rule);
  }
  .contact {
    position: absolute; left: 220px; bottom: 34px;
    font-family: "Arimo", sans-serif; color: var(--ink); font-size: 13px;
    list-style: none; line-height: 1.55;
  }
  .contact__name { font-size: 16px; margin-bottom: 4px; }
  .contact__row { display: flex; align-items: center; gap: 8px; }
  .contact__icon { width: 12px; height: 12px; flex: none; }
</style>
</head>
<body>
<main class="canvas">

  <section class="card card--tagline" aria-label="Card back">
    <div class="wordmark"><span class="wordmark__dot"></span>Mia Adores Polish</div>
    <p class="tagline">Nails are jewels not tools</p>
  </section>

  <section class="card card--info" aria-label="Card front">
    <div class="wordmark"><span class="wordmark__dot"></span>Mia Adores Polish</div>
    <p class="job-title">Nail Technician</p>

    <div class="partner"><span>VRT</span><span class="partner__square"></span></div>
    <div class="divider"></div>

    <ul class="contact">
      <li class="contact__name">Mia Penhallow</li>
      <li class="contact__row">
        <svg class="contact__icon" viewBox="0 0 12 12" aria-hidden="true">
          <rect x="3" y="0.5" width="6" height="11" rx="1" fill="none" stroke="#111" stroke-width="1.2"/>
          <circle cx="6" cy="9.5" r="0.7" fill="#111"/>
        </svg>
        <span>077-0028-3614</span>
      </li>
      <li class="contact__row">
        <svg class="contact__icon" viewBox="0 0 12 12" aria-hidden="true">
          <rect x="0.6" y="2.5" width="10.8" height="7.5" fill="none" stroke="#111" stroke-width="1.2"/>
          <path d="M0.6 2.5 L6 6.8 L11.4 2.5" fill="none" stroke="#111" stroke-width="1.2"/>
        </svg>
        <span>miaadorespolish@brightpost.example</span>
      </li>
    </ul>
  </section>

</main>
</body>
</html>
```